Business card design needed

I need a business card design for a new online retail business based in Australia. I am unsure of the exact content of what I will be selling but it will be probably women's clothing, accessories, gym wear, gifts and maybe homeware linen. I am wanting a classy design that portrays the image of class/style/upmarket.

Target Market(s)

predominantely women - 20-50 age group

Industry/Entity Type

Retail

Contact Information for Business Card

Purely Lustre
Karen Whitlow
Director
ABN 73215548906
17 Harcourt Lane Dunmore Ridge NSW 2291
ph: +61 427 390 845
sales@purelylustre.com.au

Logo Text

I am open for suggestions here

Requirements
Must have
• The design must be both sides of the card

```html
<!DOCTYPE html>
<html lang="en">
<head>
<meta charset="utf-8">
<title>Purely Lustre – Business Card</title>
<link rel="stylesheet" href="https://fonts.googleapis.com/css2?family=Josefin+Slab:wght@400;700&family=Advent+Pro:wght@400;500&display=swap">
<style>
  :root {
    --paper: #ffffff;
    --frame: #6b6b6b;
    --card-light: #f1f1f3;
    --card-mid: #dcdce0;
    --plum-deep: #2a0724;
    --plum: #5b1452;
    --magenta: #b3168f;
    --magenta-soft: #d35db7;
    --mauve: #9c5b92;
    --slate: #565456;
    --silver: #c9c9cc;
    --ink-grey: #7d7d80;
    --lavender-faint: #cdbfd3;
    --text-light: #f6ecf4;
  }
  * { margin: 0; padding: 0; box-sizing: border-box; }
  html, body { width: 1200px; height: 742px; overflow: hidden; background: var(--paper); }
  .canvas {
    position: relative;
    width: 1200px; height: 742px;
    background: var(--paper);
    border: 1px solid var(--frame);
  }
  .card {
    position: absolute;
    left: 304px;
    width: 538px; height: 311px;
    overflow: hidden;
    background: linear-gradient(120deg, var(--paper) 10%, var(--card-light) 55%, var(--card-mid) 100%);
  }
  .card--front { top: 58px; }
  .card--back { top: 377px; }
  .card__art { position: absolute; inset: 0; width: 100%; height: 100%; }
  .brand-name {
    position: absolute;
    font-family: "Josefin Slab", serif;
    font-weight: 700;
    white-space: nowrap;
  }
  .card--front .brand-name {
    left: 28px; top: 34px;
    font-size: 25px;
    color: var(--plum);
  }
  .card--back .brand-name {
    left: 0; right: 0; top: 30px;
    text-align: center;
    font-size: 27px;
    color: var(--lavender-faint);
  }
  .brand-dot {
    display: inline-block;
    width: 9px; height: 9px;
    border-radius: 50%;
    background: currentColor;
    margin-right: 8px;
    vertical-align: 3px;
  }
  .holder {
    position: absolute;
    left: 360px; top: 33px;
    width: 150px;
    text-align: center;
    font-family: "Josefin Slab", serif;
    color: var(--ink-grey);
  }
  .holder__name { font-size: 16px; font-weight: 400; line-height: 1.1; }
  .holder__role { font-size: 12px; line-height: 1.2; }
  .contact {
    position: absolute;
    left: 16px;
    font-family: "Advent Pro", sans-serif;
    font-weight: 500;
    color: var(--text-light);
    font-size: 14px;
    white-space: nowrap;
    text-transform: uppercase;
    letter-spacing: 0.2px;
  }
  .contact--address { top: 254px; }
  .contact--web { top: 279px; }
  .contact span + span { margin-left: 10px; }
  .contact--web span + span { margin-left: 30px; }
  .offer {
    position: absolute;
    left: 0; right: 0; top: 256px;
    text-align: center;
    font-family: "Advent Pro", sans-serif;
    font-weight: 500;
    font-size: 17px;
    color: var(--text-light);
    white-space: nowrap;
  }
  .offer li { display: inline; list-style: none; margin: 0 4px; }
  .offer li::before { content: "★"; font-size: 13px; margin-right: 1px; }
  .abn {
    position: absolute;
    left: 0; right: 0; top: 285px;
    text-align: center;
    font-family: "Advent Pro", sans-serif;
    font-size: 13px;
    color: var(--text-light);
  }
</style>
</head>
<body>
<main class="canvas">

  <section class="card card--front" aria-label="Front of business card">
    <svg class="card__art" viewBox="0 0 538 311" preserveAspectRatio="none" aria-hidden="true">
      <defs>
        <radialGradient id="front-band" cx="0.5" cy="0.35" r="0.8">
          <stop offset="0" stop-color="var(--magenta)"/>
          <stop offset="0.45" stop-color="var(--plum)"/>
          <stop offset="1" stop-color="var(--plum-deep)"/>
        </radialGradient>
        <linearGradient id="silver-line" x1="0" x2="1">
          <stop offset="0" stop-color="var(--silver)"/>
          <stop offset="0.5" stop-color="#ffffff"/>
          <stop offset="1" stop-color="var(--silver)"/>
        </linearGradient>
      </defs>
      <path class="wave-band" d="M0,250 C90,268 180,248 215,195 C250,140 320,120 365,160 C410,200 455,225 538,160 L538,311 L0,311 Z" fill="url(#front-band)"/>
      <path class="wave-edge" d="M0,244 C90,262 180,242 212,190 C248,135 322,114 368,155" fill="none" stroke="url(#silver-line)" stroke-width="5"/>
      <path class="wave-edge" d="M368,155 C412,196 455,222 538,158" fill="none" stroke="var(--plum)" stroke-width="2"/>
    </svg>
    <svg class="card__art" viewBox="0 0 538 311" preserveAspectRatio="none" role="img" aria-label="Decorative silver and magenta swirl ornaments along the wave">
      <defs>
        <radialGradient id="swirl-magenta">
          <stop offset="0" stop-color="var(--magenta-soft)" stop-opacity="0.9"/>
          <stop offset="1" stop-color="var(--magenta)" stop-opacity="0"/>
        </radialGradient>
        <radialGradient id="swirl-silver">
          <stop offset="0" stop-color="var(--silver)" stop-opacity="0.7"/>
          <stop offset="1" stop-color="var(--silver)" stop-opacity="0"/>
        </radialGradient>
      </defs>
      <ellipse cx="290" cy="210" rx="80" ry="60" fill="url(#swirl-magenta)"/>
      <ellipse cx="470" cy="170" rx="60" ry="45" fill="url(#swirl-magenta)"/>
      <ellipse cx="90" cy="175" rx="90" ry="60" fill="url(#swirl-silver)"/>
    </svg>

    <p class="brand-name"><span class="brand-dot"></span>Purely Lustre</p>

    <div class="holder">
      <p class="holder__name">Karen Whitlow</p>
      <p class="holder__role">Director</p>
    </div>

    <p class="contact contact--address"><span>17 Harcourt Lane Dunmore Ridge NSW 2291</span><span>Ph: +61 427 390 845</span></p>
    <p class="contact contact--web"><span>www.purelylustre.com.au</span><span>E-mail: sales@purelylustre.com.au</span></p>
  </section>

  <section class="card card--back" aria-label="Back of business card">
    <svg class="card__art" viewBox="0 0 538 311" preserveAspectRatio="none" aria-hidden="true">
      <defs>
        <radialGradient id="back-band" cx="0.45" cy="0.45" r="0.75">
          <stop offset="0" stop-color="var(--magenta-soft)"/>
          <stop offset="0.45" stop-color="var(--mauve)"/>
          <stop offset="1" stop-color="var(--slate)"/>
        </radialGradient>
      </defs>
      <path class="wave-band" d="M0,215 C70,205 150,185 205,150 C250,122 310,122 345,160 C385,205 490,215 538,125 L538,311 L0,311 Z" fill="url(#back-band)"/>
      <path class="wave-edge" d="M0,210 C70,200 150,180 203,146 C250,118 312,118 348,156" fill="none" stroke="url(#silver-line)" stroke-width="5"/>
    </svg>
    <svg class="card__art" viewBox="0 0 538 311" preserveAspectRatio="none" role="img" aria-label="Decorative silver and pink swirl ornaments along the wave">
      <ellipse cx="270" cy="185" rx="85" ry="60" fill="url(#swirl-magenta)" opacity="0.7"/>
      <ellipse cx="55" cy="185" rx="70" ry="45" fill="url(#swirl-silver)"/>
    </svg>

    <p class="brand-name"><span class="brand-dot"></span>Purely Lustre</p>

    <ul class="offer">
      <li>Women's Clothing</li><li>Accessories</li><li>Gym Wear</li><li>GIFTS</li><li>Homeware</li>
    </ul>
    <p class="abn">ABN 73215548906</p>
  </section>

</main>
</body>
</html>
```